TRV Mechanical Solutions Business Card Design

Business card design

Thinking just large logo on one side with a phone number and the back side is contact info with services we offer with a industrial plant across the bottom of the card

See must haves. I will be laser etching these business cards on black metal business cards as well as full color card stock. So must be bold and professional.

Target Market(s)

Industrial manufacturing

Contact Information for Business Card

Industrial manufacturing construction business specializing in consulting project managment and completing projects turn key

Font styles to use
Other font styles liked:
• See Logo for colors and font style

Requirements
Must have
• TRV Mechanical Solutions
• Gerald Munroe
• 2847 Alderwick Lane
• Bel Air, MD, 21047
• Project Managment
• Consulting
• Turn Key Industrial Projects
• I’d like a industrial manufacturing “cityline” on the back side bottom of the
• I’d like to be able to print these business cards in regular color on card stock but I’d also like the design to be etched into black metal business cards

```html
<!DOCTYPE html>
<html lang="en">
<head>
<meta charset="utf-8">
<title>TRV Mechanical Solutions – Business Cards</title>
<link rel="stylesheet" href="https://fonts.googleapis.com/css2?family=Michroma&display=swap">
<style>
  :root {
    --bg: #3a3a3a;
    --card-black: #111111;
    --card-black-glow: #2c2c2c;
    --card-white: #ffffff;
    --brand-blue: #2c55a8;
    --steel: #4a4a4a;
    --steel-light: #6a6a6a;
    --ink: #333333;
    --silver: #e8e8e8;
  }
  * { box-sizing: border-box; margin: 0; padding: 0; }
  html, body { width: 1200px; height: 1000px; overflow: hidden; }
  body {
    background: var(--bg);
    font-family: "Michroma", sans-serif;
    position: relative;
  }
  .card {
    position: absolute;
    left: 250px;
    width: 700px;
    height: 400px;
    overflow: hidden;
    box-shadow: 0 10px 30px rgba(0,0,0,.5);
  }
  .brand-name {
    white-space: nowrap;
    text-transform: uppercase;
    letter-spacing: 0.5px;
    line-height: 1;
  }

  /* Front: black metal side */
  .card-front {
    top: 50px;
    background: radial-gradient(ellipse at 50% 35%, var(--card-black-glow), var(--card-black) 70%);
    color: var(--silver);
  }
  .front-brand {
    position: absolute;
    top: 140px; left: 0; right: 0;
    display: flex; align-items: center; justify-content: center; gap: 16px;
  }
  .front-brand .brand-square {
    width: 30px; height: 30px;
    border: 3px solid var(--silver);
    flex: none;
  }
  .front-brand .brand-name { font-size: 22px; }
  .front-rule {
    position: absolute;
    top: 200px; left: 110px; right: 110px;
    height: 1px;
    background: linear-gradient(90deg, transparent, #888, transparent);
  }
  .front-phone {
    position: absolute;
    top: 232px; left: 0; right: 0;
    display: flex; align-items: center; justify-content: center; gap: 14px;
    font-size: 22px; letter-spacing: 1px;
  }

  /* Back: full colour side */
  .card-back {
    top: 550px;
    background: var(--card-white);
    color: var(--ink);
  }
  .back-shape { position: absolute; inset: 0; }
  .back-brand {
    position: absolute;
    top: 72px; left: 55px;
    display: flex; align-items: center; gap: 10px;
  }
  .back-brand .brand-square {
    width: 22px; height: 22px;
    border: 3px solid var(--brand-blue);
    flex: none;
  }
  .back-brand .brand-name { color: var(--brand-blue); font-size: 16px; }
  .back-rule {
    position: absolute; top: 112px; left: 55px; width: 360px; height: 1px;
    background: linear-gradient(90deg, transparent, #999, transparent);
  }
  .contact { position: absolute; top: 182px; left: 60px; }
  .contact-name {
    color: var(--brand-blue);
    font-size: 15px;
    text-transform: uppercase;
    padding-bottom: 6px;
    border-bottom: 2px solid var(--brand-blue);
    display: inline-block;
    margin-bottom: 8px;
  }
  .contact-address { font-size: 11px; line-height: 1.7; color: var(--ink); }
  .divider {
    position: absolute; top: 168px; left: 330px;
    width: 2px; height: 80px; background: var(--brand-blue);
  }
  .services { position: absolute; top: 168px; left: 350px; }
  .services-title {
    color: var(--brand-blue); font-size: 13px; text-transform: uppercase; margin-bottom: 8px;
  }
  .services-list { list-style: none; font-size: 10.5px; line-height: 1.9; }
  .services-list li { display: flex; align-items: center; gap: 8px; }
  .services-list li::before {
    content: ""; width: 6px; height: 6px; background: var(--brand-blue); flex: none;
  }
  .cityline {
    position: absolute; left: 0; bottom: 0;
    width: 640px; height: 90px;
    background: linear-gradient(180deg, var(--steel-light), var(--steel));
  }
</style>
</head>
<body>

  <section class="card card-front">
    <div class="front-brand">
      <span class="brand-square"></span>
      <span class="brand-name">TRV Mechanical Solutions</span>
    </div>
    <div class="front-rule"></div>
    <div class="front-phone">
      <svg width="24" height="24" viewBox="0 0 24 24" aria-hidden="true">
        <circle cx="12" cy="12" r="11" fill="none" stroke="#e8e8e8" stroke-width="1.5"/>
        <path d="M8 6.5c.6-.4 1.2-.3 1.5.3l1 1.9c.2.5.1 1-.3 1.3l-.7.6c.6 1.3 1.6 2.4 2.9 3l.6-.7c.3-.4.9-.5 1.3-.3l1.9 1c.6.3.7.9.3 1.5l-.8 1c-.5.6-1.3.8-2 .5-3-1.2-5.3-3.5-6.5-6.5-.3-.7-.1-1.5.5-2z" fill="#e8e8e8"/>
      </svg>
      <span class="phone-number">55 418 3067</span>
    </div>
  </section>

  <section class="card card-back">
    <svg class="back-shape" width="700" height="400" viewBox="0 0 700 400" aria-hidden="true">
      <path d="M560 0 Q660 170 665 400 L700 400 L700 0 Z" fill="#2c55a8"/>
      <path d="M548 0 Q648 170 653 400" fill="none" stroke="#444444" stroke-width="10"/>
    </svg>

    <div class="back-brand">
      <span class="brand-square"></span>
      <span class="brand-name">TRV Mechanical Solutions</span>
    </div>
    <div class="back-rule"></div>

    <div class="contact">
      <div class="contact-name">Gerald Munroe</div>
      <div class="contact-address">2847 Alderwick Lane<br>Bel Air, MD, 21047</div>
    </div>

    <div class="divider"></div>

    <div class="services">
      <div class="services-title">Services We Offer</div>
      <ul class="services-list">
        <li>Project Managment</li>
        <li>Consulting</li>
        <li>Turn Key Industrial Projects</li>
      </ul>
    </div>

    <div class="cityline" role="img" aria-label="Industrial plant skyline silhouette with cooling towers, chimneys and factory buildings"></div>
  </section>

</body>
</html>
```